Walk Bright through the Seasons: 52 Weeks to a Year of Courage and Calm

This is a non-fiction, self-help book. The first edition was published a decade ago, and it needs a new design. Nothing too literal (no actual hearts on the cover) but something inspirational or perhaps something quite plain. The current cover is below for reference, but I DO NOT want something similar to that. It is outdated.

The cover must include:

1. Title: Walk Bright through the Seasons
2. Subtitle: 52 Weeks to a Year of Courage and Calm
3. Author Name: Tobin Wells

It should also have plenty of "white space" in other words the fonts shouldnt be so big that they take up the whole cover.

Dimensions: 9" x 6.25"

Target Market(s)

adults interested in personal development

Font styles to use
Serif
Script

Colors

Designer to choose colors to be used in the design.

Requirements
Must have
• Classic look and feel. The current design is too busy. I have included examples of the style I like below. I'm open to a singular graphic/photo but nothing more than that. Probably plain text is best.
• Please look at the samples I have included of best-selling books in the genre that I like. The cover should be modeled after these.

```html
<!DOCTYPE html>
<html lang="en">
<head>
<meta charset="utf-8">
<title>Walk Bright through the Seasons — Tobin Wells</title>
<link rel="stylesheet" href="https://fonts.googleapis.com/css2?family=Crimson+Pro:ital,wght@0,400;0,700;1,400&family=Montserrat:wght@400;500&display=swap">
<style>
  :root {
    --backdrop: #cbcbcb;
    --paper: #ffffff;
    --brand-blue: #0f7bc2;
    --ink: #111111;
    --metal-light: #f4f4f4;
    --metal-dark: #a3a3a3;
  }
  * { margin: 0; padding: 0; box-sizing: border-box; }
  html, body {
    width: 1200px; height: 1200px; overflow: hidden;
    background: var(--backdrop);
  }
  .cover {
    position: absolute; left: 259px; top: 89px;
    width: 682px; height: 1022px;
    background: var(--paper);
    text-align: center;
  }
  .subtitle {
    position: absolute; top: 150px; left: 0; right: 0;
    font-family: "Crimson Pro", Georgia, serif;
    font-style: italic; font-weight: 400;
    font-size: 27px; line-height: 34px;
    color: var(--ink);
  }
  .title { font-weight: 400; }
  .title-word {
    position: absolute; left: 0; right: 0;
    font-family: "Montserrat", Arial, sans-serif;
    font-weight: 500; font-size: 84px; line-height: 1;
    letter-spacing: 0.05em;
    color: var(--brand-blue);
  }
  .title-word--walk { top: 262px; }
  .title-word--bright { top: 362px; }
  .title-connector {
    position: absolute; top: 466px; left: 0; right: 0;
    font-family: "Crimson Pro", Georgia, serif;
    font-style: italic; font-weight: 400;
    font-size: 40px; line-height: 1;
    color: var(--ink);
  }
  .title-word--seasons { top: 522px; }
  .emblem {
    display: inline-block; width: 0.74em; height: 0.74em;
    margin: 0 0.02em;
    vertical-align: -0.04em; border-radius: 50%;
    background: radial-gradient(circle at 40% 38%, var(--metal-light) 0 55%, var(--metal-dark) 82%, #d6d6d6 100%);
  }
  .endorsement {
    position: absolute; top: 742px; left: 0; right: 0;
    font-family: "Crimson Pro", Georgia, serif;
    color: var(--ink);
  }
  .endorsement__quote {
    font-style: italic; font-weight: 400;
    font-size: 20px; line-height: 26px;
  }
  .endorsement__source { margin-top: 8px; font-size: 20px; font-weight: 400; }
  .endorsement__source strong { font-weight: 700; }
  .endorsement__source em { font-style: italic; }
  .author-band {
    position: absolute; left: 0; right: 0; bottom: 0; height: 114px;
    background: var(--brand-blue);
    display: flex; align-items: center; justify-content: center;
  }
  .author-name {
    font-family: "Montserrat", Arial, sans-serif;
    font-weight: 400; font-size: 42px; letter-spacing: 0.07em;
    color: var(--paper);
  }
</style>
</head>
<body>
  <main class="cover">
    <p class="subtitle">52 Weeks to a Year of<br>Courage and Calm</p>
    <h1 class="title">
      <span class="title-word title-word--walk">WALK</span>
      <span class="title-word title-word--bright">BRIGHT</span>
      <span class="title-connector">through the</span>
      <span class="title-word title-word--seasons">SE<span class="emblem" role="img" aria-label="Silver compass emblem standing in for the letter A"></span>SONS</span>
    </h1>
    <blockquote class="endorsement">
      <p class="endorsement__quote">“This warm, wonderful, and inspiring book,<br>will give you courage and calm in every area of your life.”</p>
      <p class="endorsement__source">– <strong>Dana Merritt</strong> best-selling author of <em>“Clear the Morning”</em></p>
    </blockquote>
    <footer class="author-band">
      <p class="author-name">TOBIN WELLS</p>
    </footer>
  </main>
</body>
</html>
```